Business card for a shipping supplies business

Needing a business card design. Please see the logo. The logo with the white font should be used if there is a dark background.

We are looking for the following info on the card. Please see the sample info. We will need the info to be changed with a few different employee names and info but all will use the same template.

Business Name: The Crate Heron
Employee Name : Marcus Delaney
Position: Account Manager
Address: 4827 W. Ridge 418 S.
Fort Worth, TX 73948
email: Marcus@thecrateheron.example
telephone: 855-619-2740 x 207
website: www.getparcelkits.example

Target Market(s)

Businesses who ship products for online sales

Industry/Entity Type

Cardboard

Contact Information for Business Card

Name, title, address, website, logo, telephone number

Font styles to use
Sans Serif

Colors
EE7325
F08F49
F5BC92
FAE3D3
FDF4ED

Requirements
Must have
• Logo on back of card. Clean look, just logo, website address

```html
<!DOCTYPE html>
<html lang="en">
<head>
<meta charset="utf-8">
<title>The Crate Heron – Business Card</title>
<link href="https://fonts.googleapis.com/css2?family=Raleway:wght@300;400;700;800&display=swap" rel="stylesheet">
<style>
  :root {
    --orange: #EE7325;
    --tan: #DAAE91;
    --cream: #FAE3D3;
    --ink: #1B1B1D;
    --white: #FFFFFF;
    --paper: #FFFFFF;
  }
  html, body { margin: 0; padding: 0; overflow: hidden; background: var(--paper); }
  .stage { position: relative; width: 1200px; height: 1200px; overflow: hidden; background: var(--paper); font-family: 'Raleway', sans-serif; }
  .card { position: absolute; left: 246px; width: 709px; height: 425px; overflow: hidden; }
  .card--front { top: 150px; }
  .card--back { top: 598px; }
  .card__art { position: absolute; inset: 0; width: 100%; height: 100%; display: block; }
  .brand { position: absolute; display: flex; flex-direction: column; align-items: center; }
  .brand__dot { border-radius: 50%; background: var(--orange); }
  .brand__name { color: var(--white); font-weight: 700; letter-spacing: 0.04em; white-space: nowrap; line-height: 1; }
  .card--front .brand { left: 0; width: 563px; top: 98px; }
  .card--front .brand__dot { width: 78px; height: 78px; margin-bottom: 22px; }
  .card--front .brand__name { font-size: 27px; }
  .card--back .brand { left: 420px; width: 256px; top: 143px; }
  .card--back .brand__dot { width: 100px; height: 100px; margin-bottom: 26px; }
  .card--back .brand__name { font-size: 33px; }
  .website { position: absolute; left: 0; width: 574px; margin: 0; text-align: center; color: var(--white); font-weight: 700; font-size: 16px; }
  .card--front .website { top: 380px; }
  .identity { position: absolute; left: 50px; top: 66px; color: var(--white); }
  .identity__company { font-size: 24px; font-weight: 800; margin: 0; line-height: 1.1; }
  .identity__rule { width: 154px; height: 2px; margin: 8px 0 10px; background: linear-gradient(90deg, var(--cream) 0 51%, transparent 51% 52%, var(--cream) 52%); }
  .identity__name { font-size: 24px; font-weight: 800; margin: 0; line-height: 1.1; }
  .identity__title { font-size: 14px; font-weight: 400; margin: 2px 0 0; }
  .contact { position: absolute; left: 50px; top: 228px; list-style: none; margin: 0; padding: 0; color: var(--white); font-size: 12px; font-weight: 300; line-height: 18px; letter-spacing: -0.01em; }
  .contact__item { display: flex; align-items: center; gap: 12px; margin-bottom: 14px; white-space: nowrap; }
  .contact__item:last-child { margin-top: 16px; }
  .contact__icon { width: 18px; height: 18px; flex: none; }
</style>
</head>
<body>
<main class="stage">

  <section class="card card--front" aria-label="Card front">
    <svg class="card__art" viewBox="0 0 886 531" preserveAspectRatio="none" aria-hidden="true">
      <rect width="886" height="531" fill="var(--orange)"/>
      <path d="M0 0H886V255C700 320 480 425 275 420C160 417 60 390 0 355Z" fill="var(--tan)"/>
      <path d="M0 0H886V235C700 300 500 420 300 420C170 418 70 340 0 255Z" fill="var(--orange)"/>
      <path d="M0 0H886V215C700 290 500 418 330 418C180 416 70 320 0 215Z" fill="var(--cream)"/>
      <path d="M0 0H886V40C700 180 520 410 330 412C180 414 80 220 0 38Z" fill="var(--ink)"/>
      <path d="M886 0V22C700 140 560 290 478 352" fill="none" stroke="var(--tan)" stroke-width="8"/>
    </svg>
    <div class="brand">
      <span class="brand__dot" aria-hidden="true"></span>
      <span class="brand__name">CRATE HERON</span>
    </div>
    <p class="website">www.getparcelkits.example</p>
  </section>

  <section class="card card--back" aria-label="Card back">
    <svg class="card__art" viewBox="0 0 886 531" preserveAspectRatio="none" aria-hidden="true">
      <rect width="886" height="531" fill="var(--orange)"/>
      <path d="M440 0H886V531H375C345 470 332 400 334 335C337 220 400 90 440 0Z" fill="var(--tan)"/>
      <path d="M450 0H886V531H410C365 480 336 410 336 335C338 220 410 90 450 0Z" fill="var(--orange)"/>
      <path d="M460 0H886V531H455C380 490 338 420 337 335C338 220 420 90 460 0Z" fill="var(--cream)"/>
      <path d="M580 0H886V531H565C420 470 340 420 338 335C336 240 450 110 580 0Z" fill="var(--ink)"/>
      <path d="M582 0C500 90 420 180 370 260" fill="none" stroke="var(--tan)" stroke-width="5"/>
    </svg>

    <div class="identity">
      <h1 class="identity__company">The Crate Heron</h1>
      <div class="identity__rule"></div>
      <h2 class="identity__name">Marcus Delaney</h2>
      <p class="identity__title">Account Manager</p>
    </div>

    <ul class="contact">
      <li class="contact__item">
        <svg class="contact__icon" viewBox="0 0 20 20" aria-hidden="true"><path d="M10 1a6 6 0 0 0-6 6c0 4.5 6 12 6 12s6-7.5 6-12a6 6 0 0 0-6-6zm0 8.5A2.5 2.5 0 1 1 10 4.5a2.5 2.5 0 0 1 0 5z" fill="var(--white)"/></svg>
        <span>4827 W. Ridge 418 S.<br>Fort Worth, TX 73948</span>
      </li>
      <li class="contact__item">
        <svg class="contact__icon" viewBox="0 0 20 20" aria-hidden="true"><g fill="none" stroke="var(--white)" stroke-width="1.8"><circle cx="10" cy="10" r="8"/><path d="M2 10h16M10 2c-3 3-3 13 0 16M10 2c3 3 3 13 0 16"/></g></svg>
        <span>www.getparcelkits.example<br>Marcus@thecrateheron.example</span>
      </li>
      <li class="contact__item">
        <svg class="contact__icon" viewBox="0 0 20 20" aria-hidden="true"><path d="M2 7c0-2 3-3 8-3s8 1 8 3v1.5h-4V7H6v1.5H2zM5 10h10l2 6H3z" fill="var(--white)"/></svg>
        <span>855-619-2740 x 207</span>
      </li>
    </ul>

    <div class="brand">
      <span class="brand__dot" aria-hidden="true"></span>
      <span class="brand__name">CRATE HERON</span>
    </div>
  </section>

</main>
</body>
</html>
```